Project Sign for Construction Company

Site contractor needs a 4'x8' sign to place on construction sites for advertising. Our company builds the infrastructure for new housing developments. These sign will be posted on the road side to be viewed by passing cars. I want a clean and bold look and feel that resembles my company logo.

Font styles to use
Other font styles liked:
• Hypatia Sans Pro

Colors

Designer to choose colors to be used in the design.

Requirements
Must have
• 555-382-9146 | Info@MarlowPaving.example
• CUC 8047319
• www.MarlowPaving.example
• Services
• Road Construction
• Site Preparation & Excavation
• Underground Utilities
• Shoreline Restoration
Nice to have
• Now Hiring
• Pipe Layers
• Foremen
• Equipment Operators
Should not have
• Should not have stock picture images used in the design, focus on logo and geometric shapes

```html
<!DOCTYPE html>
<html lang="en">
<head>
<meta charset="utf-8">
<title>Marlow Paving – Site Sign</title>
<link href="https://fonts.googleapis.com/css2?family=Montserrat:wght@500;600;700;800&family=Oswald:wght@700&display=swap" rel="stylesheet">
<style>
  :root {
    --brand-blue: #0a57a3;
    --blue-soft: #2f74bb;
    --white: #ffffff;
    --panel-light: #f4f5f7;
    --panel-shade: #dcdee2;
    --ink-gray: #77787b;
    --page-bg: #e9eaec;
  }
  * { margin: 0; padding: 0; box-sizing: border-box; }
  html, body {
    width: 1200px; height: 720px; overflow: hidden;
    background: var(--page-bg);
    font-family: "Montserrat", Arial, sans-serif;
  }
  .sign {
    position: absolute; left: 40px; top: 80px;
    width: 1120px; height: 560px; overflow: hidden;
    background: linear-gradient(160deg, var(--panel-shade) 0%, var(--panel-light) 35%, var(--white) 70%, var(--panel-light) 100%);
  }
  .sign-shapes { position: absolute; inset: 0; }
  .megaphone-art {
    position: absolute; left: 115px; top: 48px; width: 140px; height: 218px;
    border-radius: 14px;
    background: radial-gradient(circle at 60% 50%, var(--blue-soft), var(--brand-blue) 75%);
  }
  .hiring-headline {
    position: absolute; left: 262px; top: 66px;
    transform: rotate(-8deg); transform-origin: left bottom;
    color: var(--white); font-family: "Oswald", "Arial Narrow", sans-serif; font-weight: 700;
    line-height: 0.95; text-transform: uppercase;
  }
  .hiring-headline .now { display: block; font-size: 40px; margin-left: 76px; }
  .hiring-headline .hiring { display: block; font-size: 78px; letter-spacing: 3px; }
  .job-list {
    position: absolute; left: 408px; top: 214px; list-style: none;
    color: var(--brand-blue); font-weight: 800; font-size: 30px;
    font-variant: small-caps; line-height: 36.5px; letter-spacing: 0.3px;
  }
  .job-list li { position: relative; padding-left: 31px; }
  .job-list .arrow { position: absolute; left: 0; top: 11px; width: 20px; height: 16px; }
  .job-list .continued { padding-left: 31px; }
  .services {
    position: absolute; left: 131px; top: 362px; color: var(--white);
  }
  .services h2 { font-size: 36px; font-weight: 700; letter-spacing: 0.5px; margin-bottom: 8px; }
  .services ul { list-style: none; }
  .services li {
    font-size: 21px; font-weight: 700; font-variant: small-caps;
    line-height: 25.5px; letter-spacing: 0.8px; position: relative; padding-left: 24px;
  }
  .services li::before {
    content: ""; position: absolute; left: 1px; top: 9px;
    width: 8px; height: 8px; border-radius: 50%; background: var(--white);
  }
  .brand-block {
    position: absolute; left: 735px; top: 150px; width: 385px;
    text-align: center; color: var(--brand-blue);
  }
  .brand-block .mark {
    display: block; width: 34px; height: 34px; margin: 0 auto 18px;
    background: var(--brand-blue);
  }
  .brand-block .brand-name {
    font-size: 50px; font-weight: 800; line-height: 1.05; letter-spacing: 3px;
  }
  .contact {
    position: absolute; left: 735px; top: 380px; width: 385px;
    text-align: center; color: var(--ink-gray); font-weight: 700;
  }
  .contact .phone {
    color: var(--brand-blue); font-size: 44px; font-weight: 800; letter-spacing: 0.5px;
    line-height: 56px; margin-bottom: 2px;
  }
  .contact .line { font-size: 22px; font-variant: small-caps; line-height: 30px; }
</style>
</head>
<body>
  <main class="sign">
    <svg class="sign-shapes" viewBox="0 0 1120 560" width="1120" height="560" aria-hidden="true">
      <polygon class="blue-field" points="0,0 769,0 665,560 0,560" fill="#0a57a3"/>
      <g class="guide-lines" stroke="#ffffff" stroke-width="1.6" fill="none">
        <line x1="651" y1="560" x2="749" y2="0"/>
        <line x1="0" y1="68" x2="198" y2="68"/>
        <line x1="553" y1="68" x2="764" y2="68"/>
        <line x1="55" y1="51" x2="55" y2="560"/>
        <line x1="0" y1="536" x2="670" y2="536"/>
        <line x1="552" y1="91" x2="665" y2="25"/>
        <line x1="31" y1="398" x2="212" y2="286"/>
      </g>
      <line class="contact-rule" x1="735" y1="368" x2="1120" y2="368" stroke="#7d7e81" stroke-width="2.5"/>
      <path class="job-panel" d="M400,203 L695,203 L667,369 L440,369 C408,369 386,345 380,310 L367,232 C364,214 376,203 400,203 Z" fill="#ffffff"/>
    </svg>

    <div class="megaphone-art" role="img" aria-label="Sketched megaphone with a burst shape announcing hiring"></div>

    <h1 class="hiring-headline"><span class="now">Now</span><span class="hiring">Hiring</span></h1>

    <ul class="job-list">
      <li><svg class="arrow" viewBox="0 0 20 16"><path d="M0,5.5 H10 V0 L20,8 L10,16 V10.5 H0 Z" fill="#0a57a3"/></svg>Pipe Layers</li>
      <li><svg class="arrow" viewBox="0 0 20 16"><path d="M0,5.5 H10 V0 L20,8 L10,16 V10.5 H0 Z" fill="#0a57a3"/></svg>Foremen</li>
      <li><svg class="arrow" viewBox="0 0 20 16"><path d="M0,5.5 H10 V0 L20,8 L10,16 V10.5 H0 Z" fill="#0a57a3"/></svg>Equipment</li>
      <li class="continued">Operators</li>
    </ul>

    <section class="services">
      <h2>SERVICES</h2>
      <ul>
        <li>Road Construction</li>
        <li>Site Preparation &amp; Excavation</li>
        <li>Underground Utilities</li>
        <li>Shoreline Restoration</li>
      </ul>
    </section>

    <div class="brand-block">
      <span class="mark"></span>
      <div class="brand-name">MARLOW<br>PAVING</div>
    </div>

    <div class="contact">
      <div class="phone">555-382-9146</div>
      <div class="line">Info@MarlowPaving.example</div>
      <div class="line">CUC 8047319</div>
      <div class="line">www.MarlowPaving.example</div>
    </div>
  </main>
</body>
</html>
```